Clear Coat 5L & 2.5L kit

Clear coat 5 Liter with 2.5 Liter hardener
I attached few examples
Required size:
5L
Actual size is: 22.875 x 10.4375 inch
With bleed added: 23.125 x 10.6875 inch
2.5L
Actual size is: 22.875 x 6.1875 inch
With bleed added: 23.125x6.2125 inch

Thanks

```html
<!DOCTYPE html>
<html lang="en">
<head>
<meta charset="utf-8">
<title>Nova Finish Apex – Clear Coat Kit Labels</title>
<link rel="stylesheet" href="https://fonts.googleapis.com/css2?family=Montserrat:wght@700;800&family=Arimo:wght@400;700&display=swap">
<style>
  :root {
    --backdrop: #f4f4f6;
    --charcoal: #333338;
    --sun-yellow: #ffd338;
    --sky-blue: #009bd1;
    --white: #ffffff;
  }
  html, body {
    margin: 0;
    padding: 0;
    width: 1200px;
    height: 1118px;
    overflow: hidden;
    background: var(--backdrop);
  }
  .kit {
    display: block;
    width: 1200px;
    height: 1118px;
  }
  .brand-name {
    font-family: "Montserrat", sans-serif;
    font-weight: 800;
    fill: var(--charcoal);
  }
  .line-name {
    font-family: "Montserrat", sans-serif;
    font-weight: 800;
    fill: var(--white);
  }
  .product-title {
    font-family: "Arimo", sans-serif;
    font-weight: 700;
    fill: var(--white);
  }
  .product-detail {
    font-family: "Arimo", sans-serif;
    font-weight: 400;
    fill: var(--white);
  }
  .tagline {
    font-family: "Arimo", sans-serif;
    font-weight: 700;
    fill: var(--charcoal);
  }
  .spec-box {
    fill: none;
    stroke: var(--white);
    stroke-width: 1.5;
  }
  .band-dark { fill: var(--charcoal); }
  .band-yellow { fill: var(--sun-yellow); }
  .band-blue { fill: var(--sky-blue); }
</style>
</head>
<body>
<svg class="kit" viewBox="0 0 1200 1118" xmlns="http://www.w3.org/2000/svg">

  <!-- 5 L clear coat label -->
  <g class="label label-clear-coat">
    <rect class="band-yellow" x="221" y="165" width="458" height="817"/>
    <rect class="band-dark" x="221" y="180" width="458" height="28"/>
    <polygon class="band-dark" points="221,580 679,634 679,910 221,910"/>
    <rect class="band-dark" x="221" y="958" width="458" height="24"/>

    <text class="brand-name" x="340" y="416" font-size="68" letter-spacing="1">NOVA</text>
    <text class="brand-name" x="341" y="462" font-size="38" letter-spacing="8">FINISH</text>

    <text class="line-name" x="455" y="636" font-size="66" letter-spacing="30" text-anchor="middle">APEX</text>

    <text class="product-title" x="457" y="761" font-size="36" text-anchor="middle">CLEAR COAT</text>
    <text class="product-detail" x="457" y="801" font-size="32" text-anchor="middle">2:1 MIX</text>
    <text class="product-detail" x="457" y="832" font-size="20" text-anchor="middle">2.1 VOC</text>

    <text class="tagline" x="453" y="939" font-size="12.5" text-anchor="middle">HIGH GLOSS | GOOD LEVELING | EASY APPLICATION</text>
  </g>

  <!-- 2.5 L hardener label -->
  <g class="label label-hardener">
    <rect class="band-blue" x="723" y="415" width="322" height="575"/>
    <rect class="band-dark" x="723" y="425" width="322" height="20"/>
    <polygon class="band-dark" points="723,707 1045,745 1045,940 723,940"/>
    <rect class="band-dark" x="723" y="974" width="322" height="16"/>

    <text class="brand-name" x="806" y="590" font-size="48" letter-spacing="1">NOVA</text>
    <text class="brand-name" x="807" y="623" font-size="27" letter-spacing="6">FINISH</text>

    <text class="line-name" x="880" y="744" font-size="42" letter-spacing="22" text-anchor="middle">APEX</text>

    <text class="product-title" x="892" y="819" font-size="27" letter-spacing="6" text-anchor="middle">HARDENER</text>
    <text class="product-title" x="891" y="838" font-size="15" text-anchor="middle">FOR CLEAR COAT</text>

    <rect class="spec-box" x="837" y="866" width="106" height="24"/>
    <line class="spec-box" x1="890" y1="866" x2="890" y2="890"/>
    <text class="product-title" x="863" y="883" font-size="11" text-anchor="middle">2:1 MIX</text>
    <text class="product-title" x="916" y="883" font-size="11" text-anchor="middle">2.1 VOC</text>

    <text class="tagline" x="889" y="960" font-size="8.5" text-anchor="middle">HIGH GLOSS | GOOD LEVELING | EASY APPLICATION</text>
  </g>

</svg>
</body>
</html>
```